Chateau de Vormelle Investment Brochure

I need a brochure that can be used both online and as printed version to direct people to which explains the investment opportunity at Chateau de Vormelle. We are offering shares in the chateau, its operating company and 4 weeks 5 star accommodation per annum in a suite of the investors choice. The design should appeal to people looking at holiday homes but also be serious enough to attract investors.

Target Market(s)

Affluent 35+ seeking investment opportunity

Industry/Entity Type

Investment

```html
<!DOCTYPE html>
<html lang="en">
<head>
<meta charset="utf-8">
<title>Chateau de Vormelle – Investment Brochure</title>
<link href="https://fonts.googleapis.com/css2?family=Montserrat:wght@300;400&family=Noto+Serif:ital,wght@0,400;1,400;1,700&display=swap" rel="stylesheet">
<style>
  :root {
    --backdrop: #e6e4e1;
    --paper: #ffffff;
    --ink: #3a3a3a;
    --ink-soft: #555555;
    --brand-blue: #1f6db5;
  }
  * { box-sizing: border-box; margin: 0; padding: 0; }
  html, body { width: 1200px; height: 941px; overflow: hidden; background: var(--backdrop); }
  body { position: relative; font-family: "Montserrat", Arial, sans-serif; color: var(--ink); }

  .spread { position: absolute; left: 38px; width: 1118px; height: 395px; background: var(--paper); overflow: hidden; box-shadow: 0 2px 6px rgba(0,0,0,.18); }
  .spread--investment { top: 33px; }
  .spread--area { top: 472px; }

  .photo { position: absolute; }
  .photo--round { width: 156px; height: 156px; border-radius: 50%; left: 582px; top: 23px; }

  .feature-list { position: absolute; left: 399px; top: 61px; width: 112px; font-family: "Noto Serif", Georgia, serif; font-style: italic; font-size: 8.8px; line-height: 11.2px; color: var(--ink); list-style: none; }
  .feature-list li { margin-bottom: 10px; }
  .feature-list li::before { content: "·"; }

  .caption { position: absolute; right: 746px; top: 317px; text-align: right; font-family: "Noto Serif", Georgia, serif; color: #222; }
  .caption__title { font-size: 13px; letter-spacing: .3px; line-height: 17px; }
  .caption__sub { font-size: 13px; font-style: italic; line-height: 17px; }

  .display-title { position: absolute; left: 606px; font-family: "Noto Serif", Georgia, serif; font-style: italic; font-weight: 400; color: var(--brand-blue); white-space: nowrap; }
  .display-title--loan { top: 213px; font-size: 20px; line-height: 29px; }
  .display-title--area { top: 231px; font-size: 23px; line-height: 32px; }

  .column { position: absolute; left: 792px; width: 298px; font-size: 7.2px; line-height: 9px; font-weight: 400; color: var(--ink-soft); }
  .column--investment { top: 49px; }
  .column--area { top: 44px; }
  .column__heading { font-family: "Noto Serif", Georgia, serif; font-style: italic; font-size: 10.2px; line-height: 13px; color: var(--brand-blue); margin-bottom: 9px; }
  .column p { margin-bottom: 9px; }
  .elements { list-style: none; padding-left: 6px; }
  .elements li { margin-bottom: 9px; }
  .split { list-style: none; padding-left: 6px; margin-bottom: 9px; }
  .split li { display: flex; align-items: baseline; }
  .split .leader { flex: 1; border-bottom: 1px dotted var(--ink-soft); margin: 0 1px; transform: translateY(-2px); }

  .column--area p { text-align: justify; margin-bottom: 7px; }
  .column--area p.quote { font-family: "Noto Serif", Georgia, serif; font-style: italic; font-weight: 700; font-size: 10px; line-height: 13px; color: var(--brand-blue); margin-bottom: 16px; padding-right: 18px; text-align: left; }

  .wordmark { position: absolute; right: 30px; bottom: 20px; display: flex; align-items: center; gap: 4px; font-size: 4.6px; letter-spacing: 1px; text-transform: uppercase; color: var(--ink-soft); }
  .wordmark__dot { width: 5px; height: 5px; border: 0.6px solid var(--ink-soft); }
</style>
</head>
<body>

<section class="spread spread--investment">
  <div class="photo" style="left:44px;top:45px;width:160px;height:121px;background:linear-gradient(160deg,#d9d7d2,#8e9297 60%,#6e6a63);" role="img" aria-label="Fitted grey kitchen with integrated appliances in a suite"></div>
  <div class="photo" style="left:216px;top:45px;width:160px;height:121px;background:linear-gradient(150deg,#b9b4ad,#e8e3dd 55%,#8a6c52);" role="img" aria-label="Bedroom with double bed and wooden chair"></div>
  <div class="photo" style="left:44px;top:180px;width:160px;height:121px;background:linear-gradient(150deg,#d6d6d6,#f2f2f2 50%,#2a2a2a);" role="img" aria-label="En-suite bathroom with basins and black tiled shower"></div>
  <div class="photo" style="left:216px;top:180px;width:160px;height:121px;background:radial-gradient(circle at 50% 60%,#1b1a16 20%,#6f6a55 45%,#4f6a35 80%);" role="img" aria-label="Stone cave entrance in the château moat"></div>

  <ul class="feature-list">
    <li>Fully furnished and equipped suites</li>
    <li>All suites have a kitchen with quality integrated appliances</li>
    <li>All bedrooms are en-suite</li>
    <li>A lockable owner's cupboard is available with every suite to keep personal belongings between stays</li>
    <li>Each suite is allocated a lockable cave in the château moat for storing larger items such as bikes, wine etc.</li>
  </ul>

  <div class="caption">
    <div class="caption__title">TURNKEY SERVICE</div>
    <div class="caption__sub">dedicated storage space and cave</div>
  </div>

  <div class="photo photo--round" style="background:radial-gradient(circle at 45% 40%,#e3c1a0,#6fa6c4 45%,#b9a98a 75%);" role="img" aria-label="Relaxed man leaning back at a laptop outdoors"></div>

  <h2 class="display-title display-title--loan">Loan<br>repayment -<br>estimated<br>after 20 years</h2>

  <div class="column column--investment">
    <h3 class="column__heading">Investment in the château involves 3 elements</h3>
    <ol class="elements">
      <li>1. Share purchase in the SARL Château de Vormelle (accommodation rental company)</li>
      <li>2. Share purchase in SCI Gardiens du Château de Vormelle (the property owner)</li>
      <li>3. Long term loan to the SCI Gardiens du Château de Vormelle for the development of the estate</li>
    </ol>
    <p>For illustrative purposes a €100k investment &nbsp;representing 3.0% of the SARL and 1.5% of the<br>SARL would be split as follows:</p>
    <ul class="split">
      <li>1. Share purchase in SARL Château de Vormelle<span class="leader"></span>€360.00</li>
      <li>2. Share purchase in SCI Gardiens du Château de Vormelle<span class="leader"></span>€15.03</li>
      <li>3. Long term loan to SCI<span class="leader"></span>€99,624.97</li>
    </ul>
    <p>The bulk of the investment is in the form of a loan to the SCI. &nbsp;It is estimated that this would be paid back in 2035.</p>
  </div>

  <div class="photo" style="left:792px;top:239px;width:298px;height:102px;background:linear-gradient(180deg,#3c5a8c,#7d8fa8 45%,#c9c2a8 62%,#3f4a34);" role="img" aria-label="The château and its stone bridge under a blue sky"></div>

  <div class="wordmark"><span class="wordmark__dot"></span>Chateau de Vormelle</div>
</section>

<section class="spread spread--area">
  <div class="photo" style="left:0;top:0;width:240px;height:132px;background:linear-gradient(180deg,#6d86a3,#d9cfb4 60%,#7c8a6a);" role="img" aria-label="Abbey church with bell tower"></div>
  <div class="photo" style="left:0;top:134px;width:240px;height:129px;background:linear-gradient(160deg,#6b6158,#d8cfc4 50%,#b98c86);" role="img" aria-label="Painted medieval tomb effigies in the abbey"></div>
  <div class="photo" style="left:0;top:265px;width:240px;height:130px;background:linear-gradient(160deg,#5a5236,#9a8f78 55%,#cfc7b8);" role="img" aria-label="Old wooden wine press in a stone cellar"></div>
  <div class="photo" style="left:241px;top:0;width:317px;height:263px;background:linear-gradient(180deg,#9fb4c4,#b8aa90 40%,#9a8a72 75%,#4e6a32);" role="img" aria-label="Château with round towers in the valley"></div>
  <div class="photo" style="left:241px;top:265px;width:317px;height:130px;background:linear-gradient(180deg,#c8c0b6,#e9e6e2 55%,#a9a39b);" role="img" aria-label="Restaurant table set with cups and wine glasses"></div>

  <div class="photo photo--round" style="background:radial-gradient(circle at 50% 45%,#d7b79b,#e7a7c4 40%,#8fb06a 75%);" role="img" aria-label="Couple cycling in helmets through the countryside"></div>

  <h2 class="display-title display-title--area">The<br>Surrounding<br>Area</h2>

  <div class="column column--area">
    <p class="quote">“ Served by its own village of Varennes-le-Clos with its mellow limestone buildings, you can enjoy a typical French country lifestyle with cafes, bars, boulangerie and friendly local people. ”</p>
    <p>In the midst of a National Park, you are an easy 12 mile drive from Saint-Aubrac, the equestrian centre of France, famed for its National Riding School with its ‘Écuyers Noirs’ &nbsp;dressage display team - on a par with the Royal Riding academy. Saint-Aubrac is also the home to many wine producers whose ‘caves’; hewn out of the rock; line the Verlaine river. &nbsp;Culturally astute, the Aubracoise people have recently renovated their impressive classically styled theatre where they play hosts to visiting orchestras and theatre companies. &nbsp;And there are plenty of museums and galleries to keep you interested too.</p>
    <p>Gastronomy is not in short supply with many restaurants in the area finding favour in the Guide Étoile</p>
    <p>We are a short drive to Abbaye de Saint-Orlan – final resting place of King Aldric the Bold and of his mother Mathilde of Orsanne</p>
    <p>The Chateau is in the heart of the Verlaine Valley, the Garden of France, renowned for its abundance of vineyards (Valmoray, Chênelle, Bourlanne, Musclair) and Chateaux (Brissel, Brézac, Ambreuil, Ambolay).</p>
    <p>Great watersports, parachuting, golf and ballooning, not to mention excellent cycling and rambling trails</p>
    <p>For the kids; a day visit to the conservation - friendly Zoo at Doulay la Source is a ‘must’ receiving as it does, unanimous approval from younger guests. Whilst the recently opened Forest Lodges park offers day tickets.</p>
  </div>

  <div class="wordmark"><span class="wordmark__dot"></span>Chateau de Vormelle</div>
</section>

</body>
</html>
```